KLD Rafter bench flyer for Vantor Machinery

Design a flyer that will be used on social media to promote our KLD Portal bench. This is to promote our tables to new market and under a new brand name. Design should we print the flyer to be on a 11x8.5 paper.
Included is the two accepted logo configuration of our brand - Vantor Machinery along with 2 photos of our latest installation. If you can change the logo on the installation from Pilsk Holdings to Vantor Machinery please.
Highlights of our machine to be included on flyer:
- Available in 12’ or 14’ wide
- Side or end eject
Highlights of our machine to add to flyer if your design can incorporate it:
- Heavy duty table top.
- T-slot opening for jigging
- All tables built to customers length requirements

For contact information to be put on flyer, Deshawn at (800)555-0192 or deshawn@pilskhold.example
Will have the website address added here as soon as it is done.

Please incorporate the following line (will prefer to have this at the bottom) : Vantor Machinery a brand manufactured by Pilsk Holdings Inc.

Our equipment colors are Clam white and Orange like seen on the equipment pictures.

Target Market(s)

Truss Manufacturers

Industry/Entity Type

Pre fabricated housing market and component manufacturers

Font styles to use
Sans Serif

Colors
EE7325
F08F49
F5BC92
FAE3D3
FDF4ED

Requirements
Must have
• a few highlights that are in the description
Nice to have
• Added to project description

```html
<!DOCTYPE html>
<html lang="en">
<head>
<meta charset="utf-8">
<title>KLD Portal Bench Flyer – Vantor Machinery</title>
<link rel="stylesheet" href="https://fonts.googleapis.com/css2?family=Montserrat:ital,wght@0,400;0,500;0,600;0,700;0,800;1,800&display=swap">
<style>
  :root {
    --orange: #EE7325;
    --orange-mid: #F08F49;
    --orange-soft: #F5BC92;
    --cream: #FAE3D3;
    --cream-light: #FDF4ED;
    --brown: #4B3A2C;
    --brown-deep: #3A2C21;
    --ink: #3d3d3d;
    --white: #ffffff;
    --backdrop: #e9e9ea;
  }
  * { box-sizing: border-box; margin: 0; padding: 0; }
  html, body { width: 1200px; height: 2220px; overflow: hidden; }
  body {
    background: var(--backdrop);
    font-family: "Montserrat", Arial, sans-serif;
    position: relative;
  }
  .flyer {
    position: absolute; left: 0; top: 300px;
    width: 1200px; height: 1620px;
    background: var(--white);
    overflow: hidden;
  }
  .header {
    position: absolute; left: 0; top: 0; width: 1200px; height: 290px;
    background: var(--orange);
  }
  .header-shape { position: absolute; left: 0; top: 0; }
  .brand {
    position: absolute; left: 70px; top: 95px;
    display: flex; align-items: center; gap: 22px;
  }
  .brand-square { width: 60px; height: 60px; background: var(--white); }
  .brand-name {
    color: var(--white); font-weight: 800; font-size: 50px;
    line-height: 1; letter-spacing: 1px; text-transform: uppercase;
  }
  .brand-note {
    position: absolute; left: 760px; top: 100px; width: 380px;
    color: var(--white); font-size: 24px; font-weight: 500; line-height: 1.35;
  }
  .hero-photo {
    position: absolute; left: 0; top: 290px; width: 1200px; height: 640px;
    background: linear-gradient(160deg, #8a8f93 0%, #c9c6bf 40%, #e7ddcf 65%, #a58c6e 100%);
  }
  .hero-overlay { position: absolute; left: 0; top: 290px; }
  .title {
    position: absolute; left: 560px; top: 370px;
    color: var(--white); font-weight: 800; font-style: italic;
    font-size: 92px; line-height: 1.02; text-transform: uppercase;
    text-shadow: 0 3px 10px rgba(0,0,0,.35);
  }
  .features {
    position: absolute; left: 0; top: 930px; width: 640px; height: 250px;
    background: var(--cream-light);
    padding: 40px 0 0 70px;
  }
  .feature { display: flex; align-items: center; gap: 26px; margin-bottom: 30px; }
  .feature-icon {
    width: 78px; height: 78px; background: var(--orange);
    display: flex; align-items: center; justify-content: center;
  }
  .feature-text {
    color: var(--orange); font-weight: 800; font-size: 34px;
    line-height: 1.1; text-transform: uppercase;
  }
  .contact {
    position: absolute; left: 640px; top: 930px; width: 560px; height: 250px;
    background: var(--brown);
    padding: 65px 0 0 80px; color: var(--white);
  }
  .contact-label { font-size: 32px; font-weight: 600; letter-spacing: 2px; text-transform: uppercase; }
  .contact-phone { display: flex; align-items: center; gap: 16px; margin-top: 18px; font-size: 46px; font-weight: 800; }
  .highlights-band {
    position: absolute; left: 0; top: 1195px; width: 590px; height: 66px;
    background: var(--orange);
    clip-path: polygon(0 0, 100% 0, 94% 100%, 0 100%);
    color: var(--white); font-weight: 800; font-size: 28px;
    letter-spacing: 1px; text-transform: uppercase;
    display: flex; align-items: center; padding-left: 70px;
  }
  .highlights-list { position: absolute; left: 70px; top: 1274px; width: 520px; list-style: none; }
  .highlight {
    display: flex; align-items: center; gap: 24px;
    padding: 10px 0; border-bottom: 2px solid var(--cream);
    color: var(--ink); font-size: 21px; font-weight: 600; line-height: 1.25;
    text-transform: uppercase;
  }
  .highlight:last-child { border-bottom: none; }
  .tick {
    flex: none; width: 44px; height: 44px; border: 3px solid var(--orange);
    display: flex; align-items: center; justify-content: center;
  }
  .detail-photo {
    position: absolute; left: 630px; top: 1210px; width: 570px; height: 300px;
    background: linear-gradient(135deg, #d7cfc3 0%, #f1e9dd 45%, #e39a5f 75%, #9c8f80 100%);
  }
  .footer {
    position: absolute; left: 0; top: 1510px; width: 1200px; height: 110px;
    background: var(--brown-deep);
    display: flex; align-items: center; justify-content: space-between; gap: 40px;
    padding: 0 60px; color: var(--white);
    font-size: 29px; font-weight: 700;
  }
  .footer-item { display: flex; align-items: center; gap: 18px; white-space: nowrap; }
  .footer-icon {
    flex: none;
    width: 56px; height: 56px; border-radius: 50%; border: 3px solid var(--orange);
    display: flex; align-items: center; justify-content: center;
  }
</style>
</head>
<body>
  <main class="flyer">
    <header class="header">
      <svg class="header-shape" width="1200" height="290" viewBox="0 0 1200 290" aria-hidden="true">
        <polygon points="0,0 520,0 380,290 0,290" fill="var(--orange-mid)"/>
        <polygon points="640,0 1200,0 1200,60 610,60" fill="var(--orange-soft)" opacity=".35"/>
      </svg>
      <div class="brand">
        <span class="brand-square"></span>
        <span class="brand-name">Vantor Machinery</span>
      </div>
      <p class="brand-note">Vantor Machinery a brand manufactured by Pilsk Holdings Inc.</p>
    </header>

    <div class="hero-photo" role="img" aria-label="Photo of the KLD Portal bench installed in a truss manufacturing plant"></div>
    <svg class="hero-overlay" width="1200" height="640" viewBox="0 0 1200 640" aria-hidden="true">
      <polygon points="0,380 300,640 0,640" fill="var(--orange)"/>
      <polygon points="0,300 60,300 420,640 340,640 0,330" fill="var(--orange-mid)" opacity=".85"/>
      <polygon points="520,40 1200,40 1200,250 470,250" fill="rgba(58,44,33,.35)"/>
    </svg>
    <h1 class="title">KLD<br>Portal Bench</h1>

    <section class="features">
      <div class="feature">
        <span class="feature-icon">
          <svg width="46" height="46" viewBox="0 0 46 46" aria-hidden="true"><path d="M4 23h38M4 23l9-9M4 23l9 9M42 23l-9-9M42 23l-9 9" stroke="#fff" stroke-width="4" fill="none" stroke-linecap="round" stroke-linejoin="round"/></svg>
        </span>
        <span class="feature-text">Available in<br>12’ or 14’ wide</span>
      </div>
      <div class="feature">
        <span class="feature-icon">
          <svg width="46" height="46" viewBox="0 0 46 46" aria-hidden="true"><path d="M6 34h34M23 8v20M15 20l8 8 8-8" stroke="#fff" stroke-width="4" fill="none" stroke-linecap="round" stroke-linejoin="round"/></svg>
        </span>
        <span class="feature-text">Side or end eject</span>
      </div>
    </section>

    <section class="contact">
      <p class="contact-label">Contact : Deshawn</p>
      <p class="contact-phone">
        <svg width="40" height="40" viewBox="0 0 24 24" aria-hidden="true"><path d="M6.6 10.8a15 15 0 0 0 6.6 6.6l2.2-2.2a1 1 0 0 1 1-.25 11.4 11.4 0 0 0 3.6.57 1 1 0 0 1 1 1V20a1 1 0 0 1-1 1A17 17 0 0 1 3 4a1 1 0 0 1 1-1h3.5a1 1 0 0 1 1 1c0 1.25.2 2.45.57 3.6a1 1 0 0 1-.25 1z" fill="var(--orange)"/></svg>
        (800)555-0192
      </p>
    </section>

    <h2 class="highlights-band">Highlights of our machine</h2>
    <ul class="highlights-list">
      <li class="highlight"><span class="tick"><svg width="26" height="26" viewBox="0 0 26 26" aria-hidden="true"><path d="M4 14l6 6L22 6" stroke="var(--orange)" stroke-width="4" fill="none" stroke-linecap="round" stroke-linejoin="round"/></svg></span>Heavy duty table top</li>
      <li class="highlight"><span class="tick"><svg width="26" height="26" viewBox="0 0 26 26" aria-hidden="true"><path d="M4 14l6 6L22 6" stroke="var(--orange)" stroke-width="4" fill="none" stroke-linecap="round" stroke-linejoin="round"/></svg></span>T-slot opening for jigging</li>
      <li class="highlight"><span class="tick"><svg width="26" height="26" viewBox="0 0 26 26" aria-hidden="true"><path d="M4 14l6 6L22 6" stroke="var(--orange)" stroke-width="4" fill="none" stroke-linecap="round" stroke-linejoin="round"/></svg></span>All tables built to customers length requirements</li>
    </ul>
    <div class="detail-photo" role="img" aria-label="Photo of a long orange and white bench line in the installation"></div>

    <footer class="footer">
      <span class="footer-item">
        <span class="footer-icon"><svg width="30" height="30" viewBox="0 0 24 24" aria-hidden="true"><rect x="3" y="5" width="18" height="14" rx="1" fill="none" stroke="var(--orange)" stroke-width="2"/><path d="M3 6l9 7 9-7" fill="none" stroke="var(--orange)" stroke-width="2"/></svg></span>
        deshawn@pilskhold.example
      </span>
      <span class="footer-item">
        <span class="footer-icon"><svg width="30" height="30" viewBox="0 0 24 24" aria-hidden="true"><circle cx="12" cy="12" r="9" fill="none" stroke="var(--orange)" stroke-width="2"/><path d="M3 12h18M12 3c3 3 3 15 0 18M12 3c-3 3-3 15 0 18" fill="none" stroke="var(--orange)" stroke-width="2"/></svg></span>
        yourwebsite.example
      </span>
    </footer>
  </main>
</body>
</html>
```